Business Card Design - Photographer

I am a landscape photographer and I require a business card design. 

I require two designs:
1)  a double sided business card
 and
b)  a single sided business card 

The single sided design can either be the same as the double sided (with just one side having all the information)....or it can be an entire new design. Its up to you.

My corporate colours are (CMYK):

Blue   69, 32, 0, 0
Grey  72,  64,  47,  31
Green  32,  2,  91,  0
Yellow   0, 19, 92, 0
Orange  0, 39, 75, 0

Colour space in final file should be in CMYK.

The details that need to be included on the card:

- Use the provided Logo
- Name: Wiktor Nowiradzki
- Email:   sales@framesbywiktor.com.au
- Website:    framesbywiktor.com.au
- Twitter:    twitter.com/framesbywiktor
- Facebook:   facebook.com/framesbywiktor
- Mobile  0419 356 782

Please use the attached template to design the logo to the specified size, including the marked bleed lines. I have also attached my logo in PNG (transparent background) and ai format for you to use.

The final file should be:
- Photoshop version with layers so I can edit the name/text etc. All non vector files should be high resolution at 1039 x 697 pixels at 300 dpi.

I also require a file as:
- Vector based PDF

Anyway questions please contact me.

Thank you

Industry/Entity Type

Landscape

Logo styles of interest
Pictorial/Combination Logo
Abstract Logo
Wordmark Logo
Lettermark Logo
Requirements
Must have
• The details that need to be included on the card:

- Use the provided Logo
- Name: Wiktor Nowiradzki
- Email: sales@framesbywiktor.com.au
- Website: framesbywiktor.com.au
- Twitter: twitter.com/framesbywiktor
- Facebook: facebook.com/framesbywiktor
- Mobile 0419 356 782

```html
<!DOCTYPE html>
<html lang="en">
<head>
<meta charset="utf-8">
<title>Frames by Wiktor – Business Card</title>
<link href="https://fonts.googleapis.com/css2?family=Catamaran:wght@400;600;700&display=swap" rel="stylesheet">
<style>
  :root {
    --card-yellow: #fdcb18;
    --ink: #111111;
    --brand-navy: #1f3a5f;
    --sky-dark: #353d4b;
    --sky-mid: #7b7a6e;
    --sun-gold: #efc14a;
    --haze: #c9a13e;
    --hills: #5c6a36;
    --meadow: #4a5a28;
  }
  html, body {
    margin: 0;
    padding: 0;
    overflow: hidden;
    background: #ffffff;
  }
  .card {
    position: relative;
    width: 1200px;
    height: 806px;
    background: var(--card-yellow);
    overflow: hidden;
    font-family: "Catamaran", Arial, sans-serif;
    color: var(--ink);
  }
  .brand {
    position: absolute;
    left: 55px;
    top: 56px;
    width: 225px;
    display: flex;
    flex-direction: column;
    align-items: center;
    gap: 12px;
  }
  .brand-mark {
    width: 82px;
    height: 82px;
    border-radius: 50%;
    background: var(--brand-navy);
  }
  .brand-name {
    font-weight: 600;
    font-size: 21px;
    letter-spacing: 1px;
    color: var(--brand-navy);
    text-transform: uppercase;
    white-space: nowrap;
    line-height: 1;
  }
  .contact {
    position: absolute;
    left: 55px;
    top: 434px;
  }
  .contact p { margin: 0; white-space: nowrap; }
  .person-name {
    font-weight: 700;
    font-size: 42px;
    line-height: 48px;
  }
  .phone {
    font-weight: 400;
    font-size: 32px;
    line-height: 44px;
  }
  .web-links {
    margin-top: 58px;
    padding-left: 6px;
  }
  .web-links .link-strong {
    font-weight: 600;
    font-size: 27px;
    line-height: 40px;
  }
  .social-links {
    margin-top: 18px;
    padding-left: 6px;
  }
  .social-links p {
    font-weight: 400;
    font-size: 27px;
    line-height: 32px;
  }
  .camera-photo, .lens-ring {
    position: absolute;
    left: 0;
    top: 0;
  }
</style>
</head>
<body>
  <div class="card">
    <div class="brand">
      <div class="brand-mark"></div>
      <div class="brand-name">Frames by Wiktor</div>
    </div>

    <div class="contact">
      <p class="person-name">wiktor nowiradzki</p>
      <p class="phone">0419 356 782</p>
      <div class="web-links">
        <p class="link-strong">framesbywiktor.com.au</p>
        <p class="link-strong">sales@framesbywiktor.com.au</p>
      </div>
      <div class="social-links">
        <p>chirplane.com/framesbywiktor</p>
        <p>peoplepage.com/framesbywiktor</p>
      </div>
    </div>

    <svg class="camera-photo" width="1200" height="806" viewBox="0 0 1200 806" role="img" aria-label="Landscape photograph of a mountain meadow at sunset under a dark cloudy sky, cut into a camera silhouette">
      <defs>
        <linearGradient id="landscape" x1="0" y1="0" x2="0" y2="1">
          <stop offset="0" stop-color="var(--sky-dark)"/>
          <stop offset="0.3" stop-color="var(--sky-mid)"/>
          <stop offset="0.45" stop-color="var(--sun-gold)"/>
          <stop offset="0.6" stop-color="var(--haze)"/>
          <stop offset="0.75" stop-color="var(--hills)"/>
          <stop offset="1" stop-color="var(--meadow)"/>
        </linearGradient>
      </defs>
      <path d="M833 0 H1200 V806 H893 Q875 806 875 788 V181 H841 Q833 181 833 173 Z" fill="url(#landscape)"/>
    </svg>

    <svg class="lens-ring" width="1200" height="806" viewBox="0 0 1200 806" aria-hidden="true">
      <circle cx="1145" cy="420" r="174" fill="none" stroke="var(--card-yellow)" stroke-width="34"/>
    </svg>
  </div>
</body>
</html>
```